Label Design for Bra "Heron Lingerie" by Tamsel Apparel Company

The bra is packaged in a poly bag with a hanger. We require a label design for the brand name "Heron Lingerie" by Tamsel Apparel Company. The main label will be attached by a string on the bra. The size of that label will 25cm in length and 10cm wide. This is the first label the customer see's when she picks up the garment/bra. Therefore, we require an eye catching design for that. This classic full shape bra with smooth moulded double layered cups fit beautifully under t-shirts and fitted garments. The tamsel apparel company logo has been included and we would like it to feature in the label. A sample labels are also given.
Target Market(s)
Laddies 18 - 45
Industry/Entity Type
Clothing
Look and feel
Each slider illustrates characteristics of the customer's brand and the style your logo design should communicate.

```html
<!DOCTYPE html>
<html lang="en">
<head>
<meta charset="utf-8">
<title>Heron Lingerie – Bra Hang Tag</title>
<link rel="stylesheet" href="https://fonts.googleapis.com/css2?family=Abril+Fatface&family=Lobster&display=swap">
<style>
  :root {
    --ink-black: #050608;
    --hanger-white: #ffffff;
    --tag-paper: #f4f2ee;
    --brand-red: #d71920;
    --cup-light: #eab0b2;
  }
  html, body {
    margin: 0;
    padding: 0;
    overflow: hidden;
  }
  .canvas {
    position: relative;
    width: 960px;
    height: 1200px;
    background: var(--ink-black);
    overflow: hidden;
  }
  .hanger {
    position: absolute;
    inset: 0;
  }
  .hang-tag {
    position: absolute;
    left: 366px;
    top: 352px;
    width: 225px;
    height: 562px;
    background: var(--tag-paper);
    overflow: hidden;
  }
  .brand-mark {
    position: absolute;
    top: 18px;
    left: 0;
    right: 0;
    display: flex;
    flex-direction: column;
    align-items: center;
    font-family: "Lobster", cursive;
    color: var(--brand-red);
    text-align: center;
  }
  .brand-mark__row {
    display: flex;
    align-items: center;
    gap: 6px;
  }
  .brand-mark__square {
    width: 11px;
    height: 11px;
    background: var(--brand-red);
  }
  .brand-mark__name {
    font-size: 19px;
    line-height: 1.2;
  }
  .brand-mark__maker {
    font-size: 10px;
    line-height: 1.3;
  }
  .product-title {
    position: absolute;
    top: 118px;
    left: 0;
    right: 0;
    margin: 0;
    text-align: center;
    font-family: "Abril Fatface", serif;
    font-weight: 400;
    font-size: 52px;
    line-height: 1;
    color: var(--brand-red);
    letter-spacing: 1px;
  }
  .bra-artwork {
    position: absolute;
    left: 16px;
    top: 170px;
    width: 193px;
    height: 96px;
    background: linear-gradient(180deg, var(--brand-red), var(--cup-light) 50%, var(--brand-red));
    border-radius: 6px;
  }
  .features {
    position: absolute;
    top: 292px;
    left: 0;
    right: 0;
    margin: 0;
    padding: 0;
    list-style: none;
    text-align: center;
    font-family: "Lobster", cursive;
    font-size: 19px;
    line-height: 25.5px;
    color: var(--brand-red);
  }
  .eco-line {
    position: absolute;
    top: 418px;
    left: 0;
    right: 0;
    margin: 0;
    text-align: center;
    font-family: "Lobster", cursive;
    font-size: 15px;
    line-height: 22px;
    color: var(--brand-red);
  }
  .membership-badge {
    position: absolute;
    left: 78px;
    top: 476px;
    width: 68px;
    height: 68px;
    border-radius: 50%;
    background: var(--brand-red);
  }
</style>
</head>
<body>
<div class="canvas">
  <svg class="hanger" width="960" height="1200" viewBox="0 0 960 1200" aria-hidden="true">
    <path d="M396 148 C420 100 470 86 496 108 C520 130 515 170 490 192 C472 208 468 222 468 240 L468 302"
          fill="none" stroke="var(--hanger-white)" stroke-width="8" stroke-linecap="round"/>
    <rect x="156" y="314" width="646" height="646" fill="none" stroke="var(--hanger-white)" stroke-width="14"/>
  </svg>

  <article class="hang-tag">
    <div class="brand-mark">
      <div class="brand-mark__row">
        <span class="brand-mark__square"></span>
        <span class="brand-mark__name">Heron Lingerie</span>
      </div>
      <span class="brand-mark__maker">by tamsel apparel company</span>
    </div>

    <h1 class="product-title">BRA</h1>

    <div class="bra-artwork" role="img" aria-label="Red line-striped illustration of a bra on a torso outline"></div>

    <ul class="features">
      <li>Comfort fit</li>
      <li>Wrinkle-resistant</li>
      <li>Machine washable</li>
      <li>Luxury fabric</li>
    </ul>

    <p class="eco-line">Help the environment<br>buy a heron</p>

    <div class="membership-badge" role="img" aria-label="Membership badge"></div>
  </article>
</div>
</body>
</html>
```